BRIGHTPINE RV Resort needs a logo and advertising poster

We need an advertising poster for our epic RV Resort located on north end of Tolvin Lake, (Northern Saskatchewan, trees no mountains)
SEASONAL FULL SERVICE SITES with marina and lake access.
Sauna/plunge, disc golf , hiking/quad trails, and pet friendly.
We are after a fun 70,s themed simple poster. Please use brand guide for colours and redo logo to be Brightpine Resort.

Target Market(s)

RV owners looking for permeant sites. No tenting.

Font styles to use
Other font styles liked:
• See brand guide

Requirements
Must have
• Change exisiting branding to BRIGHTPINE RESORT instead of coffee Emphasis Limited sites.... Referral discount. Phone number.
Nice to have
• .
Should not have
• Keep it simple

```html
<!DOCTYPE html>
<html lang="en">
<head>
<meta charset="utf-8">
<title>Brightpine RV Resort – Poster</title>
<link rel="stylesheet" href="https://fonts.googleapis.com/css2?family=Anton&family=Roboto:wght@300;400&display=swap">
<style>
  :root {
    --green: #6a8153;
    --green-dark: #5c7748;
    --pink: #edcbd3;
    --teal: #80c3b6;
    --yellow: #ebc95b;
    --gold-line: #e4c45a;
    --ink: #2f2f2f;
    --cream: #efe6d2;
    --white: #ffffff;
  }
  * { box-sizing: border-box; margin: 0; padding: 0; }
  html, body { width: 800px; height: 1200px; overflow: hidden; background: var(--green); }
  .poster {
    position: relative; width: 800px; height: 1200px; overflow: hidden;
    background: var(--green);
    font-family: "Roboto", Arial, sans-serif; font-weight: 300; color: var(--ink);
  }
  .hero-photo {
    position: absolute; left: 0; top: 0; width: 800px; height: 640px;
    background: linear-gradient(180deg,
      #ffffff 0%, #ffffff 17%, #e9efe9 26%, #4f7a3a 34%, #6a9442 42%,
      #5ec8d6 52%, #62b9c7 58%, #6ea34a 66%, #6b974a 82%, var(--green) 100%);
  }
  .frame { position: absolute; left: 0; top: 0; }
  .brand {
    position: absolute; left: 92px; top: 58px;
    font-family: "Anton", Impact, sans-serif; font-size: 30px; line-height: 1;
    color: var(--green-dark); letter-spacing: 0.5px;
  }
  .contact { position: absolute; left: 450px; top: 36px; display: flex; align-items: center; gap: 12px; }
  .contact-label { font-size: 13px; color: var(--green-dark); font-weight: 400; }
  .contact-number {
    font-family: "Anton", Impact, sans-serif; font-size: 27px; line-height: 1.1;
    color: var(--green-dark); letter-spacing: 0.5px;
  }
  .tag {
    position: absolute; background: var(--green); color: var(--white);
    font-family: "Anton", Impact, sans-serif; display: flex; align-items: center; justify-content: center;
    border-radius: 14px; letter-spacing: 0.5px;
  }
  .tag-referral { left: 327px; top: 161px; width: 402px; height: 75px; font-size: 33px; border-top-right-radius: 0; }
  .tag-limited { left: 81px; top: 278px; width: 251px; height: 72px; font-size: 31px; border-top-left-radius: 0; }
  .rate-card {
    position: absolute; top: 388px; width: 218px; height: 506px; border-radius: 109px;
    text-align: center; padding-top: 6px;
  }
  .rate-card.nightly { left: 59px; background: var(--pink); }
  .rate-card.weekly { left: 292px; background: var(--teal); }
  .rate-card.monthly { left: 525px; background: var(--yellow); }
  .rate-photo { width: 206px; height: 206px; border-radius: 50%; margin: 0 auto; }
  .nightly .rate-photo { background: linear-gradient(180deg, #9fc08e 0%, #6b5a42 40%, #a7a9a2 65%, #5d8c3d 100%); }
  .weekly .rate-photo { background: radial-gradient(circle at 50% 55%, #d9762a 0%, #c9672a 40%, #3f5f30 75%); }
  .monthly .rate-photo { background: linear-gradient(180deg, #dfe8e6 0%, #7fa063 45%, #e5e1d4 65%, #b7b4ab 100%); }
  .rate-period { font-size: 29px; margin-top: 7px; line-height: 1.1; }
  .rate-price {
    font-family: "Anton", Impact, sans-serif; font-size: 54px; line-height: 1.15; letter-spacing: 0.5px;
  }
  .rate-note { font-size: 18.5px; line-height: 23.8px; margin-top: 4px; padding: 0 10px; }
  .welcome { position: absolute; left: 81px; top: 905px; width: 648px; text-align: center; }
  .welcome-kicker { font-size: 29px; color: var(--cream); line-height: 1.2; }
  .welcome-title {
    font-family: "Anton", Impact, sans-serif; font-size: 44px; color: var(--white);
    line-height: 1.25; letter-spacing: 0.5px;
  }
  .welcome-body { font-size: 18.5px; line-height: 24px; color: var(--white); margin: 4px auto 0; width: 610px; }
  .fee-note {
    position: absolute; left: 81px; top: 1166px; width: 648px; text-align: center;
    font-size: 17.5px; color: var(--white);
  }
</style>
</head>
<body>
<main class="poster">
  <div class="hero-photo" role="img" aria-label="Aerial view of the resort with a large blue pool, water slide, lawn chairs and surrounding trees"></div>

  <svg class="frame" width="800" height="1200" viewBox="0 0 800 1200" aria-hidden="true">
    <path d="M81 460 V128 a18 18 0 0 1 18 -18 H110" fill="none" stroke="var(--green)" stroke-width="2.5"/>
    <path d="M275 110 H711 a18 18 0 0 1 18 18 V500" fill="none" stroke="var(--green)" stroke-width="2.5"/>
    <path d="M81 960 V1118 a18 18 0 0 0 18 18 H711 a18 18 0 0 0 18 -18 V960" fill="none" stroke="var(--gold-line)" stroke-width="2.5"/>
    <path d="M81 1200 V1167 a18 18 0 0 1 18 -18 H711 a18 18 0 0 1 18 18 V1200" fill="none" stroke="var(--gold-line)" stroke-width="2.5"/>
    <rect x="451" y="38" width="46" height="46" rx="6" fill="none" stroke="var(--green-dark)" stroke-width="3"/>
    <rect x="466" y="48" width="16" height="26" rx="3" fill="none" stroke="var(--green-dark)" stroke-width="2"/>
    <circle cx="474" cy="70" r="1.5" fill="var(--green-dark)"/>
  </svg>

  <div class="brand">BRIGHTPINE RESORT</div>

  <div class="contact" style="left:510px;">
    <div>
      <p class="contact-label">PHONE NUMBER:</p>
      <p class="contact-number">(555) 014-2290</p>
    </div>
  </div>

  <div class="tag tag-referral">5% REFERRAL DISCOUNT.</div>
  <div class="tag tag-limited">LIMITED SITES</div>

  <section class="rate-card nightly">
    <div class="rate-photo" role="img" aria-label="Open-sided picnic pavilion beside a paved path and lawn"></div>
    <p class="rate-period">Nightly</p>
    <p class="rate-price">$50.00</p>
    <p class="rate-note">In addition to our 38 short-term sites, we have an extra 19 sites available for those who may be looking for an extended stay.</p>
  </section>
  <section class="rate-card weekly">
    <div class="rate-photo" role="img" aria-label="Orange camper van parked among trees"></div>
    <p class="rate-period">Weekly</p>
    <p class="rate-price">$300</p>
    <p class="rate-note">In addition to our 38 short-term sites, we have an extra 19 sites available for those who may be looking for an extended stay.</p>
  </section>
  <section class="rate-card monthly">
    <div class="rate-photo" role="img" aria-label="Row of motorhomes parked on gravel sites under trees"></div>
    <p class="rate-period">Monthly</p>
    <p class="rate-price">$675</p>
    <p class="rate-note">In addition to our 38 short-term sites, we have an extra 19 sites available for those who may be looking for an extended stay.</p>
  </section>

  <section class="welcome">
    <p class="welcome-kicker">WELCOME TO</p>
    <h1 class="welcome-title">THE BRIGHTPINE RV RESORT!</h1>
    <p class="welcome-body">If your a member of our Beach Club or simply passing through, we invite you to stay at one of our 38 deluxe RV camping sites tucked between the trees and two fishing lakes. Best of all, we are just a few steps from all the amenities at Brightpine Beach Club which are included with your stay!</p>
  </section>

  <p class="fee-note">*There is a $25 cleanup fee if sites are left in poor condition</p>
</main>
</body>
</html>
```